Akademie für Lichtwegkunde
Zielgruppe
Ich biete die beiden Seminare 'Kraftquell am Werktag' und 'Feinsinn am Werktag' an. Die Zielgruppe sind spirituell interessierte Leute.
Aufgabenstellung
Die Anzeige sollte mehr oder weniger mit den Farben meiner Webseite übereinstimmen (www.sonnenpfad-raum.ch).
Grösse der Anzeige:
breit: 121mm
hoch: 124mm
Die Anzeige sollte mein persönliches Bild und das Logo enthalten.
Text:
Feinsinn am Werktag:
Seminare zur Förderung Ihrer Intuition. Entdecken Sie Ihre eigene Medialität und lernen Sie diese gezielt im Alltag einzusetzen.
26./27. August 2017
11./12. November 2017
Kraftquell am Werktag:
Seminare für energetisches Heilen. Lernen Sie sich und andere Menschen energetisch zu begleiten.
16./17. September 2017
9./10. Dezember 2017
2 für 1 - Aktion:
Kommen Sie zu zweit und bezahlen Sie nur für eine Person
(gültig bis Ende 2017)
Webseite:
www.sonnenpfad-raum.ch
Seminarort: Grünholdau, 3286 Lorbachtal, Schweiz

```html
<!DOCTYPE html>
<html lang="de">
<head>
<meta charset="utf-8">
<title>Anzeige – Akademie für Lichtwegkunde</title>
<link rel="stylesheet" href="https://fonts.googleapis.com/css2?family=Arimo:ital,wght@0,400;0,700;1,400&display=swap">
<style>
  :root{
    --stage:#e6e6e6;
    --sheet:#b9b9b9;
    --ink:#111;
    --white:#fff;
    --blue-deep:#0a2f7a;
    --blue-mid:#1456b8;
    --orange:#ff8a1a;
    --orange-deep:#ff6a00;
    --orange-head:#ff9a14;
    --logo-blue:#1a4fb0;
    --dot-blue:#0a1cff;
    --dot-pink:#f00ac8;
  }
  *{margin:0;padding:0;box-sizing:border-box}
  html,body{width:1184px;height:1200px;overflow:hidden}
  body{background:var(--stage);font-family:"Arimo",Arial,sans-serif;color:var(--ink);position:relative}
  .ad-sheet{position:absolute;left:242px;top:38px;width:700px;height:1124px;background:var(--sheet);overflow:hidden}
  .portrait{position:absolute;left:0;top:0;width:700px;height:447px;
    background:linear-gradient(90deg,#3a3a3a 0%,#6e6e6e 30%,#9a9a9a 55%,#d6d6d6 75%,#e4e4e4 100%)}
  .abs{position:absolute;white-space:nowrap}
  .site-url{right:25px;top:18px;font-size:23px}
  .person-name{right:25px;top:61px;font-size:23px;font-style:italic}
  .venue-label{right:25px;top:226px;font-size:25px;font-weight:700}
  .venue-address{right:25px;top:264px;font-size:16px;line-height:19px;text-align:right}
  .info-band{position:absolute;left:0;top:447px;width:700px;height:282px;
    background:linear-gradient(160deg,var(--blue-deep) 0%,var(--blue-mid) 60%,var(--blue-deep) 100%)}
  .brand-tab{position:absolute;left:411px;top:352px;width:289px;height:114px;background:var(--white);
    border-radius:34px 0 0 34px;display:flex;align-items:center;justify-content:center;gap:10px}
  .brand-dot{width:22px;height:22px;border-radius:50%;background:var(--orange)}
  .brand-name{font-size:17px;font-weight:700;color:var(--logo-blue)}
  .seminar-title{left:22px;font-size:24px;font-weight:700;color:var(--orange-head);line-height:26px}
  .seminar-text{left:22px;font-size:16px;line-height:19.5px;color:var(--white)}
  .seminar-dates{font-size:16px;line-height:19.5px;color:var(--white)}
  .offer{position:absolute;left:470px;top:495px;width:226px;height:230px}
  .offer-title{left:505px;top:559px;font-size:23px;font-weight:700;color:var(--white)}
  .offer-text{left:507px;top:602px;font-size:16px;line-height:19.5px;color:var(--white)}
  .print-colors{position:absolute;left:135px;top:906px;display:flex;align-items:center;gap:13px}
  .print-colors span{width:34px;height:34px;border-radius:50%}
  .c-black{background:#000}.c-blue{background:var(--dot-blue)}.c-pink{background:var(--dot-pink)}
  .print-label{left:301px;top:910px;font-size:22px;letter-spacing:.5px}
</style>
</head>
<body>
  <div class="ad-sheet">
    <div class="portrait" role="img" aria-label="Schwarz-weiss Porträt des Seminarleiters, Kinn auf die Hände gestützt"></div>
    <div class="abs site-url">www.sonnenpfad-raum.ch</div>
    <div class="abs person-name">Lukas Wendelin</div>
    <div class="abs venue-label">Seminarort:</div>
    <div class="abs venue-address">Grünholdau, 3286<br>Lorbachtal, Schweiz</div>

    <div class="info-band"></div>
    <div class="brand-tab"><span class="brand-dot"></span><span class="brand-name">Akademie für Lichtwegkunde</span></div>

    <div class="abs seminar-title" style="top:452px">Seminare zur Förderung<br>Ihrer Intuition</div>
    <div class="abs seminar-text" style="top:519px">Feinsinn am Werktag. Entdecken Sie Ihre<br>eigene Medialität und lernen Sie diese<br>gezielt im Alltag einzusetzen.</div>
    <div class="abs seminar-dates" style="left:284px;top:562px">26./27. August&nbsp;&nbsp;&nbsp;&nbsp;&nbsp;&nbsp;2017<br>11./12. November 2017</div>

    <div class="abs seminar-title" style="top:590px">Seminar für<br>energetisches Heilen</div>
    <div class="abs seminar-text" style="top:656px">Kraftquell am Werktag. Lernen Sie sich und<br>andere Menschen energetisch zu<br>begleiten.</div>
    <div class="abs seminar-dates" style="left:286px;top:682px">16./17. September 2017<br>9./10.&nbsp;&nbsp;&nbsp;Dezember&nbsp;&nbsp;2017</div>

    <svg class="offer" viewBox="0 0 226 230" aria-hidden="true">
      <path d="M0 0 H100 A118 118 0 0 1 218 118 V118 A112 112 0 0 1 106 230 A106 106 0 0 1 0 124 Z" fill="#e07000"/>
      <path d="M14 14 H104 A112 112 0 0 1 226 120 A108 108 0 0 1 118 228 A104 104 0 0 1 14 124 Z" fill="url(#offerGrad)"/>
      <defs><linearGradient id="offerGrad" x1="0" y1="0" x2="0" y2="1">
        <stop offset="0" stop-color="#ff9a2a"/><stop offset="1" stop-color="#ff5e00"/></linearGradient></defs>
    </svg>
    <div class="abs offer-title">2 für 1 - Aktion</div>
    <div class="abs offer-text">Kommen Sie zu zweit<br>und bezahlen Sie nur<br>für eine Person (gültig<br>bis Ende 2017)</div>

    <div class="print-colors"><span class="c-black"></span><span class="c-blue"></span><span class="c-pink"></span></div>
    <div class="abs print-label">Anzeige - Morgenkurier</div>
  </div>
</body>
</html>
```